Nutrition Infographic for weight loss- key points and nutrition habits for after weight loss surgery

I need someone to put together some infographics based on some nutrition information I have put together. We are a company who do weight loss surgery for patients and I am trying to put together some resources for patients so they can look after their nutrition for the long term.

I have some info and ideas on how we can execute this on paper but I need some a creative genius with top notch design skills to help me put it together.

I am basically after two infographics- One with the nutrition information I have outlined and One with the pyramid I have illustrated. Please let me know if you need clarification on the layout. Also happy to take on board any ideas you might have too!

If more time is needed with adjustments/refinements I understand and am happy to work with you to get to a final product we are happy with.

Target Market(s)

weight loss clients- ages ranging mostly from 20-45 male and female.

Industry/Entity Type

Health Care

Colors

Designer to choose colors to be used in the design.

Requirements
Must have
• Simple, clean concepts and images are needed.
• Easy to understand layout to enhance uptake of understanding the information

```html
<!DOCTYPE html>
<html lang="en">
<head>
<meta charset="utf-8">
<title>Sometimes Foods – Nutrition Infographic</title>
<link rel="stylesheet" href="https://fonts.googleapis.com/css2?family=Source+Sans+3:wght@400&display=swap">
<style>
  :root {
    --bg: #eeecee;
    --ink: #111111;
    --connector: #c4c4c6;
    --sweets: #f7931e;
    --sweets-deep: #f26522;
    --sweets-light: #fbb040;
    --drinks: #29a9e0;
    --drinks-deep: #1e4f9c;
    --drinks-light: #5ccdef;
    --fast: #7b2d8e;
    --fast-deep: #8a2a8e;
    --fast-light: #e483c3;
    --icon-spot: rgba(255, 255, 255, 0.34);
    --font: "Source Sans 3", "Myriad Pro", Arial, sans-serif;
  }
  * { margin: 0; padding: 0; box-sizing: border-box; }
  html, body {
    width: 1200px; height: 1200px; overflow: hidden;
    background: var(--bg);
  }
  .infographic {
    position: relative; width: 1200px; height: 1200px;
    font-family: var(--font);
  }
  .diagram { position: absolute; inset: 0; }
  .icon-spot { fill: var(--icon-spot); }
  .hub-title {
    position: absolute; left: 164px; width: 220px; top: 390px;
    text-align: center; color: var(--ink);
    font-size: 43px; line-height: 51px; font-weight: 400;
  }
  .hub-title .line-2 { display: block; margin-left: -14px; }
  .hub-body {
    position: absolute; left: 84px; width: 440px; top: 491px;
    text-align: left; color: var(--ink);
    font-size: 26px; line-height: 31.8px; letter-spacing: 0.15px;
    white-space: nowrap;
  }
  .hub-body span { display: block; }
  .hub-body .indent-s { padding-left: 5px; }
  .hub-body .indent-m { padding-left: 6px; }
  .hub-body .indent-l { padding-left: 39px; }
  .category-label {
    position: absolute; font-size: 54px; line-height: 1;
    font-weight: 400; letter-spacing: 1px;
  }
  .label-sweets { left: 749px; top: 219px; color: var(--sweets); }
  .label-drinks { left: 873px; top: 545px; color: var(--drinks); }
  .label-fast { left: 796px; top: 839px; color: var(--fast); }
</style>
</head>
<body>
<main class="infographic">
  <svg class="diagram" width="1200" height="1200" viewBox="0 0 1200 1200">
    <defs>
      <radialGradient id="hub-fill" cx="45%" cy="42%" r="60%">
        <stop offset="0%" stop-color="#ffffff"/>
        <stop offset="70%" stop-color="#fafafa"/>
        <stop offset="100%" stop-color="#dcdcdc"/>
      </radialGradient>
      <linearGradient id="sweets-fill" x1="0" y1="1" x2="1" y2="0">
        <stop offset="0%" stop-color="var(--sweets-light)"/>
        <stop offset="100%" stop-color="var(--sweets-deep)"/>
      </linearGradient>
      <linearGradient id="drinks-fill" x1="0" y1="1" x2="1" y2="0">
        <stop offset="0%" stop-color="var(--drinks-light)"/>
        <stop offset="100%" stop-color="var(--drinks-deep)"/>
      </linearGradient>
      <linearGradient id="fast-fill" x1="0" y1="1" x2="1" y2="0">
        <stop offset="0%" stop-color="var(--fast-light)"/>
        <stop offset="100%" stop-color="var(--fast-deep)"/>
      </linearGradient>
      <filter id="soft-shadow" x="-30%" y="-30%" width="160%" height="160%">
        <feDropShadow dx="-6" dy="10" stdDeviation="12" flood-color="#000" flood-opacity="0.28"/>
      </filter>
    </defs>

    <g class="connectors" stroke="var(--connector)" stroke-width="54" stroke-linecap="butt">
      <line x1="400" y1="460" x2="520" y2="370"/>
      <line x1="470" y1="579" x2="600" y2="579"/>
      <line x1="400" y1="720" x2="530" y2="820"/>
    </g>

    <circle class="hub" cx="278" cy="590" r="232" fill="url(#hub-fill)" filter="url(#soft-shadow)"/>

    <g class="category sweets">
      <circle cx="590" cy="298" r="121" fill="url(#sweets-fill)" filter="url(#soft-shadow)"/>
      <circle class="icon-spot" cx="556" cy="218" r="22" role="img" aria-label="Candy floss icon"/>
      <circle class="icon-spot" cx="612" cy="206" r="20" role="img" aria-label="Cake slice icon"/>
      <circle class="icon-spot" cx="634" cy="262" r="17" role="img" aria-label="Cupcake icon"/>
      <circle class="icon-spot" cx="584" cy="284" r="20" role="img" aria-label="Ice cream cone icon"/>
      <circle class="icon-spot" cx="518" cy="316" r="22" role="img" aria-label="Ice cream cups icon"/>
      <circle class="icon-spot" cx="642" cy="328" r="26" role="img" aria-label="Doughnut icon"/>
      <circle class="icon-spot" cx="570" cy="360" r="19" role="img" aria-label="Sundae icon"/>
    </g>

    <g class="category drinks">
      <circle cx="694" cy="579" r="121" fill="url(#drinks-fill)" filter="url(#soft-shadow)"/>
      <circle class="icon-spot" cx="630" cy="546" r="20" role="img" aria-label="Soft drink can icon"/>
      <circle class="icon-spot" cx="686" cy="540" r="20" role="img" aria-label="Bottle icon"/>
      <circle class="icon-spot" cx="752" cy="540" r="22" role="img" aria-label="Beer mug icon"/>
      <circle class="icon-spot" cx="630" cy="614" r="20" role="img" aria-label="Milkshake icon"/>
      <circle class="icon-spot" cx="685" cy="610" r="22" role="img" aria-label="Juice carton icon"/>
      <circle class="icon-spot" cx="749" cy="614" r="20" role="img" aria-label="Coffee cup icon"/>
    </g>

    <g class="category fast-foods">
      <circle cx="620" cy="854" r="121" fill="url(#fast-fill)" filter="url(#soft-shadow)"/>
      <circle class="icon-spot" cx="580" cy="782" r="19" role="img" aria-label="Fries icon"/>
      <circle class="icon-spot" cx="672" cy="808" r="24" role="img" aria-label="Chicken drumstick icon"/>
      <circle class="icon-spot" cx="555" cy="854" r="24" role="img" aria-label="Burger icon"/>
      <circle class="icon-spot" cx="636" cy="862" r="20" role="img" aria-label="Bowl of chips icon"/>
      <circle class="icon-spot" cx="579" cy="914" r="20" role="img" aria-label="Hot dog icon"/>
      <circle class="icon-spot" cx="652" cy="924" r="26" role="img" aria-label="Bread rolls icon"/>
    </g>
  </svg>

  <h1 class="hub-title">SOMETIMES<span class="line-2">FOODS</span></h1>
  <p class="hub-body"><span>These may have been a big part of</span><span class="indent-s">your diet before you decided to take</span><span class="indent-m">steps to improve your health and lose</span><span>weight. Long term success does meat</span><span>some sacrifices although it does not</span><span>mean we need to avoid your</span><span class="indent-l">favourite foods forever.</span></p>

  <h2 class="category-label label-sweets">SWEETS</h2>
  <h2 class="category-label label-drinks">DRINKS</h2>
  <h2 class="category-label label-fast">FAST FOODS</h2>
</main>
</body>
</html>
```